Need a business card for a Construction and Remodeling company.
Our company logo is the fleur de lis design as thats the family crust that we use on our logos.
Heres the info it needs:

Brackmore Construction & Remodeling, LLC
Renovations * Restorations

Elwin R. Brackmore
845 North Quarry Road
Ashgrove Connecticut 06118
(203) 555.0182
CT LIC/REG: 418257

home owners, customers

```html
<!DOCTYPE html>
<html lang="en">
<head>
<meta charset="utf-8">
<title>Brackmore Construction &amp; Remodeling — Business Card</title>
<link rel="stylesheet" href="https://fonts.googleapis.com/css2?family=Raleway:wght@400;500;600;700&display=swap">
<style>
  :root {
    --backdrop: #9b9b9b;
    --card: #262626;
    --card-edge: #1b1b1b;
    --ink: #f2f2f2;
    --ink-soft: #d9d9d9;
  }
  html, body {
    margin: 0;
    padding: 0;
    width: 1200px;
    height: 1050px;
    overflow: hidden;
    background: var(--backdrop);
    font-family: "Raleway", sans-serif;
  }
  .canvas {
    position: relative;
    width: 1200px;
    height: 1050px;
    display: flex;
    align-items: center;
    justify-content: center;
  }
  .card {
    position: relative;
    width: 980px;
    height: 560px;
    background: var(--card);
    border-radius: 4px;
    box-shadow: 0 3px 0 var(--card-edge), 0 18px 40px rgba(0,0,0,0.25);
    color: var(--ink);
    box-sizing: border-box;
    padding: 88px 0 0 150px;
  }
  .brand {
    display: inline-block;
    margin: 0 0 0 30px;
  }
  .brand-name {
    display: block;
    font-weight: 700;
    font-size: 76px;
    letter-spacing: 1px;
    line-height: 0.95;
    color: var(--ink);
  }
  .brand-line {
    display: block;
    font-weight: 500;
    font-size: 20px;
    letter-spacing: 0.5px;
    line-height: 1.1;
    color: var(--ink);
    margin: 4px 0 0 -6px;
  }
  .person {
    margin: 14px 0 0 0;
    font-weight: 600;
    font-size: 29px;
    letter-spacing: 0.5px;
    line-height: 1.2;
  }
  .contact {
    margin: 16px 0 0 0;
    font-style: normal;
    font-weight: 400;
    font-size: 22px;
    line-height: 1.18;
    color: var(--ink-soft);
  }
  .contact p { margin: 0; }
  .contact .gap { margin-top: 18px; }
  .services {
    margin: 24px 0 0 0;
    font-weight: 600;
    font-size: 23px;
    letter-spacing: 0.3px;
  }
  .services .dot {
    display: inline-block;
    width: 7px;
    height: 7px;
    border-radius: 50%;
    background: var(--ink);
    vertical-align: middle;
    margin: 0 6px;
  }
</style>
</head>
<body>
  <main class="canvas">
    <article class="card">
      <header class="brand">
        <span class="brand-name">BRACKMORE</span>
        <span class="brand-line">CONSTRUCTION &amp; REMODELING, LLC</span>
      </header>
      <h1 class="person">Elwin R. Brackmore</h1>
      <address class="contact">
        <p>Brackmore Construction &amp; Remodeling, LLC</p>
        <p>845 North Quarry Road</p>
        <p>Ashgrove Connecticut 06118</p>
        <p class="gap">(203) 555.0182</p>
        <p>CT LIC/REG: 418257</p>
      </address>
      <p class="services">Renovations<span class="dot"></span>Restorations</p>
    </article>
  </main>
</body>
</html>
```